Meridian Rest Supply Needs Business Card

Looking for a very nice looking business card. Creative but not extravagant. We sell beds and pillows across the U.S. and need something professional but catchy. I have attached the logo.

Name : Dale Fenwick
Title : President
Phone : (800) 417-2964
Email: sleep@quorvana.com
Website: www.quorvana.com

Can be single-sided or double-sided
horizontal or vertical

Can use Blues/Greys

Target Market(s)

Mass Market

Industry/Entity Type

Retail

Contact Information for Business Card

Name : Dale Fenwick
Title : President
Phone : (800) 417-2964
Email: sleep@quorvana.com
Website: www.quorvana.com

Requirements
Must have
• Clean, Modern, Smooth
• Can use Blues/Greys
• On the other side without the information - have something simple like www.quorvana.com or our logo
Nice to have
• Surprise me
Should not have
• Nothing crazy, nothing cluttered

```html
<!DOCTYPE html>
<html lang="en">
<head>
<meta charset="utf-8">
<title>quorvana — Business Card</title>
<link rel="stylesheet" href="https://fonts.googleapis.com/css2?family=Raleway:wght@300;400;700&display=swap">
<style>
  :root {
    --backdrop: #e6e7e9;
    --brand-blue: #2ea3d8;
    --ink-grey: #6d6f73;
    --panel-grey: #f2f4f6;
    --stripe-grey: #f1f2f4;
    --card-white: #ffffff;
  }
  * { margin: 0; padding: 0; box-sizing: border-box; }
  html, body {
    width: 1200px; height: 900px; overflow: hidden;
    background: var(--backdrop);
    font-family: "Raleway", sans-serif;
  }
  .card-sheet {
    position: relative; width: 1200px; height: 900px;
  }
  .card {
    position: absolute; left: 285px; width: 630px; height: 360px;
    box-shadow: 0 6px 18px rgba(0,0,0,0.12);
    overflow: hidden;
  }
  .card--front { top: 70px; background: var(--brand-blue); display: flex; align-items: center; justify-content: center; }
  .card--back { top: 470px; background: var(--card-white); display: flex; }

  .brand-name {
    font-weight: 300; letter-spacing: 2px; line-height: 1;
  }
  .card--front .brand-name { color: var(--card-white); font-size: 54px; }

  .logo-panel {
    position: relative; width: 54%; height: 100%;
    background: var(--card-white);
    display: flex; align-items: center; justify-content: center;
  }
  .logo-panel .stripes { position: absolute; inset: 0; }
  .logo-panel .brand-name {
    position: relative; color: var(--brand-blue); font-size: 64px;
  }

  .contact-panel {
    width: 46%; height: 100%; background: var(--panel-grey);
    padding: 40px 30px 0 34px;
  }
  .person-name { color: var(--brand-blue); font-weight: 700; font-size: 30px; }
  .person-title { color: var(--ink-grey); font-weight: 400; font-size: 20px; margin: 6px 0 34px 22px; }
  .contact-list { list-style: none; margin-left: 22px; }
  .contact-item {
    display: flex; align-items: center; gap: 12px;
    color: var(--ink-grey); font-size: 17px; margin-bottom: 14px;
  }
  .contact-icon { width: 26px; height: 26px; flex: none; }
</style>
</head>
<body>
<main class="card-sheet">
  <section class="card card--front" aria-label="Card front">
    <span class="brand-name">quorvana</span>
  </section>

  <section class="card card--back" aria-label="Card back">
    <div class="logo-panel">
      <svg class="stripes" width="340" height="360" viewBox="0 0 340 360" aria-hidden="true">
        <g fill="var(--stripe-grey)">
          <rect x="0" y="70" width="340" height="8"/>
          <rect x="0" y="100" width="340" height="8"/>
          <rect x="0" y="130" width="340" height="8"/>
          <rect x="0" y="160" width="340" height="8"/>
          <rect x="0" y="190" width="340" height="8"/>
          <rect x="0" y="220" width="340" height="8"/>
          <rect x="0" y="250" width="340" height="8"/>
          <rect x="0" y="280" width="340" height="8"/>
          <rect x="0" y="310" width="340" height="8"/>
        </g>
      </svg>
      <span class="brand-name">quorvana</span>
    </div>

    <div class="contact-panel">
      <h1 class="person-name">Dale Fenwick</h1>
      <p class="person-title">President</p>
      <ul class="contact-list">
        <li class="contact-item">
          <svg class="contact-icon" viewBox="0 0 26 26" aria-hidden="true">
            <circle cx="13" cy="13" r="13" fill="var(--brand-blue)"/>
            <path d="M8 10c0-1 1-2 2-2h6c1 0 2 1 2 2v1h-2.5v-1h-5v1H8z M9 12h8l1 6H8z" fill="#fff"/>
          </svg>
          <span>(800) 417-2964</span>
        </li>
        <li class="contact-item">
          <svg class="contact-icon" viewBox="0 0 26 26" aria-hidden="true">
            <circle cx="13" cy="13" r="13" fill="var(--brand-blue)"/>
            <rect x="7" y="9" width="12" height="8" rx="1" fill="#fff"/>
            <path d="M7 9.5l6 4.5 6-4.5" fill="none" stroke="var(--brand-blue)" stroke-width="1.2"/>
          </svg>
          <span>sleep@quorvana.com</span>
        </li>
        <li class="contact-item">
          <svg class="contact-icon" viewBox="0 0 26 26" aria-hidden="true">
            <circle cx="13" cy="13" r="13" fill="var(--brand-blue)"/>
            <g fill="none" stroke="#fff" stroke-width="1.8">
              <rect x="10" y="6.5" width="6" height="7" rx="3"/>
              <rect x="10" y="12.5" width="6" height="7" rx="3"/>
            </g>
          </svg>
          <span>www.quorvana.com</span>
        </li>
      </ul>
    </div>
  </section>
</main>
</body>
</html>
```